Bellmont Planners, LLC Stationary

Bellmont Planners, LLC is a new financial planning and consulting company. We are looking for designs on business cards, letterhead, envelopes, and anything else that would be useful. Our preference for business card design is two sided. We are looking for a professional and clean look with incorporating the logo and patriotic feel. Thank you to all who participate and good luck!

```html
<!DOCTYPE html>
<html lang="en">
<head>
<meta charset="utf-8">
<title>Bellmont Planners, LLC — Stationery</title>
<link rel="stylesheet" href="https://fonts.googleapis.com/css2?family=Source+Sans+3:wght@400;600&family=Homemade+Apple&display=swap">
<style>
  :root {
    --navy: #123a66;
    --red: #c3232d;
    --paper: #fbfbfb;
    --ground: #ebebeb;
    --ink: #222;
    --muted: #6b7785;
  }
  * { margin: 0; padding: 0; box-sizing: border-box; }
  html, body { width: 1200px; height: 799px; overflow: hidden; background: var(--ground); }
  body { font-family: "Source Sans 3", sans-serif; color: var(--ink); position: relative; }

  .item { position: absolute; }
  .sheet { background: var(--paper); }
  .navy { background: var(--navy); }

  /* brand lockup: dot + name + tagline */
  .brand { position: absolute; display: flex; align-items: center; gap: 6px; }
  .brand-dot { width: 10px; height: 10px; border-radius: 50%; background: var(--red); flex: none; }
  .brand-text { display: flex; flex-direction: column; }
  .brand-name { font-weight: 600; color: var(--navy); letter-spacing: .06em; text-transform: uppercase; line-height: 1; }
  .brand-tag { color: var(--muted); text-transform: uppercase; letter-spacing: .12em; line-height: 1; margin-top: 3px; }
  .on-dark .brand-name { color: #fff; }
  .on-dark .brand-tag { color: #b9c6d6; }

  .brand-lg .brand-dot { width: 20px; height: 20px; }
  .brand-lg .brand-name { font-size: 24px; }
  .brand-lg .brand-tag { font-size: 5.5px; margin-top: 5px; }
  .brand-md .brand-name { font-size: 13px; }
  .brand-md .brand-tag { font-size: 3.6px; }
  .brand-sm .brand-dot { width: 7px; height: 7px; }
  .brand-sm .brand-name { font-size: 10.5px; }
  .brand-sm .brand-tag { font-size: 3px; }
  .brand-xs .brand-dot { width: 5px; height: 5px; }
  .brand-xs .brand-name { font-size: 7px; }
  .brand-xs .brand-tag { font-size: 2.4px; }

  /* CD sleeve */
  .sleeve { left: 541px; top: 58px; width: 188px; height: 185px; }
  .sleeve-notch { position: absolute; right: 0; top: 62px; width: 24px; height: 60px; background: var(--ground); border-radius: 30px 0 0 30px; }

  /* folder */
  .folder { left: 779px; top: 58px; width: 346px; height: 466px; }
  .folder-url { position: absolute; left: 0; right: 0; top: 428px; text-align: center; color: #fff; font-size: 6px; letter-spacing: .04em; }

  /* envelopes */
  .envelope-front { left: 46px; top: 344px; width: 331px; height: 162px; }
  .envelope-back { left: 46px; top: 549px; width: 331px; height: 163px; }
  .envelope-flap { position: absolute; left: 0; top: 0; }

  /* letterhead */
  .letterhead { left: 425px; top: 300px; width: 321px; height: 438px; }
  .letter-body { position: absolute; left: 33px; top: 110px; width: 252px; font-size: 6.6px; line-height: 8.1px; text-align: justify; }
  .letter-body p { margin-bottom: 8px; }
  .letter-body .address, .letter-body .salutation-line { text-align: left; }
  .signature { width: 70px; height: 16px; margin-top: 14px; display: flex; align-items: center; font-family: "Homemade Apple", cursive; font-size: 8px; color: #333; }
  .signer-title { font-family: Georgia, serif; font-size: 8px; }
  .letter-footer { position: absolute; left: 0; right: 0; bottom: 11px; text-align: center; font-size: 3.6px; color: #555; }
  .letter-bar { position: absolute; left: 0; bottom: 0; height: 6px; width: 100%; display: flex; }
  .letter-bar .bar-navy { flex: 0 0 263px; background: var(--navy); }
  .letter-bar .bar-red { flex: 1; background: var(--red); }

  /* business cards */
  .card-front { left: 866px; top: 670px; width: 119px; height: 67px; }
  .card-back { left: 1003px; top: 670px; width: 120px; height: 67px; }
  .card-person { position: absolute; left: 8px; top: 42px; font-size: 3.6px; line-height: 1.15; color: #444; }
  .card-person .person-name { font-weight: 600; color: var(--navy); font-size: 4.2px; }
  .card-person .person-role { color: var(--red); font-size: 3px; margin-bottom: 2px; }
</style>
</head>
<body>

  <!-- primary lockup -->
  <div class="brand brand-lg" style="left:118px; top:80px;">
    <span class="brand-dot"></span>
    <div class="brand-text">
      <span class="brand-name">Bellmont</span>
      <span class="brand-tag">Planners, LLC · Financial Planning and Consulting</span>
    </div>
  </div>

  <!-- CD sleeve -->
  <section class="item sleeve navy on-dark">
    <div class="brand brand-md" style="left:36px; top:84px;">
      <span class="brand-dot"></span>
      <div class="brand-text">
        <span class="brand-name">Bellmont</span>
        <span class="brand-tag">Planners, LLC · Financial Planning and Consulting</span>
      </div>
    </div>
    <div class="sleeve-notch"></div>
  </section>

  <!-- presentation folder -->
  <section class="item folder navy on-dark">
    <div class="brand brand-md" style="left:117px; top:46px;">
      <span class="brand-dot"></span>
      <div class="brand-text">
        <span class="brand-name">Bellmont</span>
        <span class="brand-tag">Planners, LLC · Financial Planning and Consulting</span>
      </div>
    </div>
    <div class="folder-url">www.bellmontplanners.com</div>
  </section>

  <!-- envelope front -->
  <section class="item envelope-front sheet">
    <div class="brand brand-sm" style="left:20px; top:24px;">
      <span class="brand-dot"></span>
      <div class="brand-text">
        <span class="brand-name">Bellmont</span>
        <span class="brand-tag">Planners, LLC · Financial Planning and Consulting</span>
      </div>
    </div>
  </section>

  <!-- envelope back -->
  <section class="item envelope-back sheet">
    <svg class="envelope-flap" width="331" height="46" viewBox="0 0 331 46" aria-hidden="true">
      <path d="M0 0 H331 L310 36 Q305 45 294 45 H37 Q26 45 21 36 Z" fill="var(--navy)"/>
      <circle cx="165.5" cy="23" r="6" fill="#8da3bd"/>
    </svg>
  </section>

  <!-- letterhead -->
  <section class="item letterhead sheet">
    <div class="brand brand-sm" style="left:27px; top:28px;">
      <span class="brand-dot"></span>
      <div class="brand-text">
        <span class="brand-name">Bellmont</span>
        <span class="brand-tag">Planners, LLC · Financial Planning and Consulting</span>
      </div>
    </div>
    <div class="letter-body">
      <p class="address">November 1, 2015<br>Mr. Dale Porter<br>58 Harbor View Road<br>Ashford, U.K 40217</p>
      <p><span class="salutation-line">Dear Mr. Porter</span><br>The first paragraph of a typical business letter is used to state the main point of the letter. Begin with a friendly opening; then quickly transition into the purpose of your letter. Use a couple of sentences to explain the purpose, but do not go in to detail until the next paragraph.</p>
      <p>Beginning with the second paragraph, state the supporting details to justify your purpose. These may take the form of background information, statistics or first-hand accounts. A few short paragraphs within the body of the letter should be enough to support your reasoning. Finally, in the closing paragraph, briefly restate your purpose and why it is important. If the purpose of your letter is related to your employment, consider ending your letter with your contact information and title if it not included on letterhead.</p>
      <p>Finally, in the closing paragraph, briefly restate your purpose and why it is important. If the purpose of your letter is related to your employment, consider ending your letter with your contact information and title if it not included on letterhead. However, if the purpose is informational, think about closing with gratitude for the reader's time.</p>
      <p class="salutation-line">Sincerely,</p>
      <div class="signature" role="img" aria-label="Handwritten signature of Nora Bell"></div>
      <div class="signer-title">President</div>
    </div>
    <div class="letter-footer">B2/114, Lakeside Park, P.O. Box 4410 Ashford | t: +1 555 014 2201 | f: +1 555 014 2202 | e: info@bellmontplanners.com | w: bellmontplanners.com</div>
    <div class="letter-bar"><span class="bar-navy"></span><span class="bar-red"></span></div>
  </section>

  <!-- business card, front -->
  <section class="item card-front navy on-dark">
    <div class="brand brand-xs" style="left:9px; top:29px;">
      <span class="brand-dot"></span>
      <div class="brand-text">
        <span class="brand-name">Bellmont</span>
        <span class="brand-tag">Financial Planning</span>
      </div>
    </div>
  </section>

  <!-- business card, back -->
  <section class="item card-back sheet">
    <div class="brand brand-xs" style="left:48px; top:6px;">
      <span class="brand-dot"></span>
      <div class="brand-text">
        <span class="brand-name">Bellmont</span>
        <span class="brand-tag">Planners, LLC</span>
      </div>
    </div>
    <div class="card-person">
      <div class="person-name">EVAN MARSH</div>
      <div class="person-role">MANAGING DIRECTOR</div>
      <div>Level 4, 210 Market Street, Ashford 40217 | t: +1 555 014 2201</div>
      <div>m: +1 555 014 2299 | e: evan@bellmontplanners.com | www.bellmontplanners.com</div>
    </div>
  </section>

</body>
</html>
```